Music Studio and Store Business Card and Logo Design

We need a business card and logo design for an existing Music Studio (Piano and Voice) which will soon expand to offer retail sheet music for all instruments including voice. The expanding store will not sell or lease instruments. We are a well known Fine Arts Studio for instruction to children, college students, and adults with 42 enrolled students and a wait list. We want something with simple elegance, but not archaic. Even a sleek modern look is okay. We do not want something childish or too fun looking because we do serve ages 5 - 62. We would also like the logo workable/transferable to signage for our new location opening in March. We like classic burgundy, black, deep blues, but are open to other suggestions. We included our studio brochure so you can get to know us a little better and some images we thought were interesting with the use of clef signs for the & and using note heads for the bottom or top of the letter "H"

Target Market(s)

All ages

Industry/Entity Type

Business

Contact Information for Business Card

H&H Music StudioPlattsburgh, NYWanda J. Haby and Osric M. Dunleavy, Owners

Requirements
Must have
• Phone Number: (480) 615-7094
• Website: www.rtcadenzaroom.example
Nice to have
• Email: lorna@rtcadenzaroom.example
Should not have
• Any instruments on the card other than piano. Instrument pix is not a necessity.

```html
<!DOCTYPE html>
<html lang="en">
<head>
<meta charset="utf-8">
<title>R&amp;T Music Studio – Business Card</title>
<link rel="stylesheet" href="https://fonts.googleapis.com/css2?family=Arimo:wght@400&display=swap">
<style>
  :root {
    --page-bg: #e9e6e6;
    --card-white: #ffffff;
    --card-black: #050505;
    --accent-red: #c8102e;
    --ink: #111111;
    --ink-light: #ffffff;
  }
  html, body {
    margin: 0;
    padding: 0;
    width: 1200px;
    height: 800px;
    overflow: hidden;
    background: var(--page-bg);
    font-family: "Arimo", Arial, sans-serif;
  }
  .card {
    position: absolute;
    left: 75px;
    top: 100px;
    width: 1050px;
    height: 600px;
    background: var(--card-white);
    overflow: hidden;
    box-shadow: 0 10px 30px rgba(0,0,0,0.18);
  }
  .card-shapes {
    position: absolute;
    inset: 0;
  }
  .brand {
    position: absolute;
    left: 290px;
    top: 88px;
    color: var(--ink);
  }
  .brand-name {
    font-size: 66px;
    font-weight: 400;
    line-height: 1;
    letter-spacing: 0.5px;
    margin: 0;
  }
  .tagline {
    font-size: 27px;
    margin: 6px 0 0 70px;
    line-height: 1.1;
  }
  .services {
    position: absolute;
    left: 40px;
    top: 212px;
    font-size: 22px;
    color: var(--ink);
    white-space: nowrap;
  }
  .owners {
    position: absolute;
    right: 580px;
    top: 370px;
    text-align: right;
    color: var(--ink-light);
  }
  .owner-name {
    font-size: 27px;
    line-height: 1.25;
    margin: 0;
  }
  .owner-role {
    font-size: 19px;
    margin: 4px 0 0;
  }
  .divider {
    position: absolute;
    left: 492px;
    top: 368px;
    width: 2px;
    height: 110px;
    background: var(--ink-light);
  }
  .contact {
    position: absolute;
    left: 512px;
    top: 370px;
    color: var(--ink-light);
    font-size: 24px;
    line-height: 1.4;
  }
  .contact p { margin: 0; }
</style>
</head>
<body>
  <div class="card">
    <svg class="card-shapes" width="1050" height="600" viewBox="0 0 1050 600" aria-hidden="true">
      <path class="black-band" d="M0,285 C360,280 760,330 1050,470 L1050,600 L0,600 Z" fill="var(--card-black)"/>
      <path class="red-swoosh" d="M60,255 C420,258 770,320 1010,430" fill="none" stroke="var(--accent-red)" stroke-width="3"/>
    </svg>

    <div class="brand">
      <h1 class="brand-name">R&amp;T Music Studio</h1>
      <p class="tagline">Music is the language of your soul</p>
    </div>

    <div class="services">♪ Piano &amp; Voice Studies ♪ Recitals ♪ Competitions ♪ Diction Coaching</div>

    <div class="owners">
      <p class="owner-name">Lorna K. Petrov</p>
      <p class="owner-name">Osric M. Dunleavy</p>
      <p class="owner-role">Owners</p>
    </div>

    <div class="divider"></div>

    <div class="contact">
      <p>Phone: (480) 615-7094</p>
      <p>Email: lorna@rtcadenzaroom.example</p>
      <p>Maplebrook, NY</p>
      <p>www.rtcadenzaroom.example</p>
    </div>
  </div>
</body>
</html>
```